Wordpress template re-design of current website

We need a WordPress template design and new look for our existing website. Our existing site it located at www.velomor.com.au We are a tech company and want a fresh, clean modern website that matches our brand, services and logo colors. Our main Services are hospitality solutions, Velomor TV solution and managed networks, more information on these can come from our existing website.

Target Market(s)

We are a tech company so must have a modern feel for new technology

Industry/Entity Type

It Company

Number of Pages Required

5+ page

Font styles to use
Sans Serif

Requirements
Must have
• Be based on a wordpress templete design and match the services that we have in our existing website, in the testimonials want a place for video testimonials as well as text. Nice clean icons used for graphics to represent services.
Nice to have
• nice visual representation of our services in the way of clean icons etc
Should not have
• Clutter

```html
<!DOCTYPE html>
<html lang="en">
<head>
<meta charset="utf-8">
<title>Velomor Wireless Internet</title>
<link href="https://fonts.googleapis.com/css2?family=Lato:wght@400;700&family=Open+Sans:wght@400;600&display=swap" rel="stylesheet">
<style>
:root{
  --navy:#02417f;
  --slate:#6b7a86;
  --slate-dark:#5c6a75;
  --icon-grey:#6b7884;
  --text:#333;
  --muted:#9aa4ae;
  --card:#f7f8fa;
  --line:#e3e6ea;
  --band:#f4f4f4;
  --white:#fff;
}
*{margin:0;padding:0;box-sizing:border-box}
html,body{width:730px;height:1200px;overflow:hidden}
body{position:relative;background:var(--white);font-family:"Open Sans",Arial,sans-serif;color:var(--text)}
h2,h3,h4{font-weight:400}
.abs{position:absolute}

/* header */
.site-header{left:0;top:0;width:730px;height:77px;background:var(--white)}
.brand{left:60px;top:20px;display:flex;align-items:center;gap:8px}
.brand-name{font-family:"Lato",sans-serif;font-weight:700;font-size:26px;color:var(--navy);line-height:1}
.brand-dot{width:14px;height:14px;border-radius:50%;background:var(--navy)}
.phone{left:508px;top:18px;display:flex;align-items:center;gap:6px;font-family:"Lato",sans-serif;font-size:11px;letter-spacing:1px;color:#222}
.portal-btn{left:608px;top:15px;width:62px;height:21px;background:var(--navy);color:var(--white);font-family:"Lato",sans-serif;font-size:8.5px;letter-spacing:1px;display:flex;align-items:center;justify-content:center}
.main-nav{left:397px;top:53px;display:flex;gap:21px;font-family:"Lato",sans-serif;font-size:8.5px;letter-spacing:.9px;color:#333}
.main-nav .active{color:var(--navy)}

/* hero */
.hero{left:0;top:77px;width:730px;height:330px;background:linear-gradient(135deg,#c6d1e4 0%,#a7b6d0 60%,#93a4c2 100%)}
.slider-arrow{top:229px;width:24px;height:24px;border-radius:50%;background:rgba(255,255,255,.85);display:flex;align-items:center;justify-content:center}
.slider-arrow.prev{left:9px;background:rgba(255,255,255,.45)}
.slider-arrow.next{left:695px}

.tagline{left:0;top:407px;width:730px;height:79px;background:var(--navy);color:var(--white);font-family:"Lato",sans-serif;font-size:14.5px;line-height:21px;text-align:center;padding-top:19px}

/* services */
.service-card{width:297px;height:84px;background:var(--card);border:1px solid var(--line)}
.service-icon{left:18px;top:18px;width:48px;height:48px;border-radius:50%;background:var(--icon-grey);display:flex;align-items:center;justify-content:center}
.service-icon.highlight{background:var(--navy)}
.service-title{left:78px;top:20px;font-family:"Lato",sans-serif;font-weight:700;font-size:10px;color:#222}
.service-text{left:78px;top:35px;width:200px;font-family:"Lato",sans-serif;font-size:9.2px;line-height:13px;color:var(--muted)}

/* testimonials */
.testimonials{left:0;top:778px;width:730px;height:235px;background:var(--band)}
.section-title{left:0;top:30px;width:730px;text-align:center;font-family:"Lato",sans-serif;font-weight:400;font-size:15px;letter-spacing:1.5px;color:#333}
.quote-card{top:72px;width:297px;height:130px;background:var(--white)}
.video-thumb{left:7px;top:7px;width:124px;height:117px;background:linear-gradient(160deg,#7fa9d4 0%,#9fbddc 100%)}
.play{width:22px;height:22px;border-radius:50%;background:rgba(255,255,255,.75);display:flex;align-items:center;justify-content:center}
.avatar{left:27px;top:23px;width:86px;height:86px;border-radius:50%;background:#c08a62}
.quote-text{left:139px;top:7px;width:150px;font-size:6.5px;line-height:10px;color:#555}
.quote-name{left:145px;top:92px;font-family:"Lato",sans-serif;font-size:8.5px;color:#333}
.quote-role{left:145px;top:106px;font-size:6.5px;color:#777}

/* footer */
.site-footer{left:0;top:1013px;width:730px;height:154px;background:var(--slate);color:var(--white)}
.footer-heading{top:28px;font-family:"Lato",sans-serif;font-weight:700;font-size:8px;letter-spacing:.3px}
.footer-text{font-size:6.5px;line-height:9px;color:#eef1f3}
.footer-links{left:251px;top:44px;list-style:none;font-size:6.5px;line-height:12px;letter-spacing:.4px}
.footer-links li::before{content:"";display:inline-block;width:3px;height:3px;border-radius:50%;background:var(--white);margin-right:9px;vertical-align:middle}
.contact-line{left:373px;display:flex;align-items:center;gap:8px;font-size:6.5px;line-height:11px}
.field{left:549px;width:120px;height:17px;background:#8a97a2;border:1px solid #9aa6b0;font-size:6.5px;padding-left:6px;display:flex;align-items:center}
.send-btn{left:622px;top:121px;width:47px;height:14px;background:var(--navy);font-size:6.5px;font-weight:600;display:flex;align-items:center;justify-content:center;letter-spacing:.3px}
.more{left:159px;top:117px;font-size:7.5px;display:flex;align-items:center;gap:4px}

.bottom-bar{left:0;top:1167px;width:730px;height:33px;background:var(--slate-dark);color:var(--white)}
.copyright{left:61px;top:12px;font-size:6.5px}
.social{left:609px;top:11px;display:flex;gap:9px}
.social span{width:9px;height:9px;border-radius:50%;background:#e8ecef;display:block}
</style>
</head>
<body>

<header class="site-header abs">
  <div class="brand abs"><span class="brand-name">Velomor</span><span class="brand-dot"></span></div>
  <div class="phone abs">
    <svg width="9" height="12" viewBox="0 0 9 12"><path d="M2 0h2l1 3-1.5 1c.6 1.6 1.4 2.7 2.5 3.5L7.5 6 9 8.5 8 11c-4 0-7.5-5-8-9.5Z" fill="#02417f"/></svg>
    1300 555 214
  </div>
  <div class="portal-btn abs">PORTAL</div>
  <nav class="main-nav abs">
    <span class="active">HOME</span><span>SERVICES</span><span>ABOUT</span><span>OUR WORK</span><span>CONTACT</span>
  </nav>
</header>

<section class="hero abs" role="img" aria-label="Close-up photo of a keyboard key printed with a wireless signal symbol"></section>
<div class="slider-arrow prev abs"><svg width="8" height="10" viewBox="0 0 8 10"><path d="M6 1 2 5l4 4" fill="none" stroke="#c8d0dc" stroke-width="1.6"/></svg></div>
<div class="slider-arrow next abs"><svg width="8" height="10" viewBox="0 0 8 10"><path d="M2 1l4 4-4 4" fill="none" stroke="#b0b8c4" stroke-width="1.6"/></svg></div>

<div class="tagline abs">We strive to out work our competition with an effective approach and a powerful skill set,<br>which is why were industry leading.</div>

<article class="service-card abs" style="left:60px;top:544px">
  <div class="service-icon abs"><svg width="16" height="16" viewBox="0 0 16 16" fill="none" stroke="#fff" stroke-width="1.3"><path d="M3 1v5a3 3 0 0 0 6 0V1"/><path d="M6 9v2a3 3 0 0 0 6 0V9"/><circle cx="12" cy="7.5" r="1.5"/></svg></div>
  <h3 class="service-title abs">HOSPITALITY SOLUTIONS</h3>
  <p class="service-text abs">Leading supplier of public access and internet billing systems.</p>
</article>
<article class="service-card abs" style="left:372px;top:544px">
  <div class="service-icon highlight abs"><svg width="16" height="14" viewBox="0 0 16 14" fill="none" stroke="#fff" stroke-width="1.3"><rect x="3" y="2" width="10" height="7"/><path d="M1 11h14"/></svg></div>
  <h3 class="service-title abs">VELOMOR TV</h3>
  <p class="service-text abs">Leading supplier of public access and internet billing systems.</p>
</article>
<article class="service-card abs" style="left:60px;top:643px">
  <div class="service-icon abs"><svg width="16" height="16" viewBox="0 0 16 16" fill="none" stroke="#fff" stroke-width="1.5"><rect x="1.5" y="1.5" width="13" height="13" rx="2"/><path d="M5.5 4.5v7M10.5 4.5v7M5.5 8h5"/></svg></div>
  <h3 class="service-title abs">HSIA SOLUTIONS</h3>
  <p class="service-text abs">Leading supplier of public access and internet billing systems.</p>
</article>
<article class="service-card abs" style="left:372px;top:643px">
  <div class="service-icon abs"><svg width="16" height="14" viewBox="0 0 16 14" fill="#fff"><rect x="6" y="0" width="4" height="4"/><rect x="0" y="10" width="4" height="4"/><rect x="6" y="10" width="4" height="4"/><rect x="12" y="10" width="4" height="4"/><path d="M7.4 4h1.2v3H14v3h-1.2V8.2H8.6V10H7.4V8.2H3.2V10H2V7h5.4Z"/></svg></div>
  <h3 class="service-title abs">MANAGED NETWORK</h3>
  <p class="service-text abs">Leading supplier of public access and internet billing systems.</p>
</article>

<section class="testimonials abs">
  <h2 class="section-title abs">TEATIMONIALS</h2>
  <article class="quote-card abs" style="left:60px">
    <div class="video-thumb abs" role="img" aria-label="Still frame of a client video testimonial"></div>
    <div class="play abs" style="left:58px;top:54px"><svg width="8" height="9" viewBox="0 0 8 9"><path d="M1 0.5 7.5 4.5 1 8.5Z" fill="#8fb0d6"/></svg></div>
    <p class="quote-text abs">Lorem ipsum dolor sit amet, consectetur adipiscing elit. Nam facilisis mollis laoreet. Ut luctus dui vitae scelerisque scelerisque. Donec ullamcorper viverra urna. Suspendisse pulvinar gravida nibh, vitae pharetra nunc faucibus vestibulum. Suspendisse</p>
    <p class="quote-name abs">Jhone Doe</p>
    <p class="quote-role abs">Contatnry Popilar sit</p>
  </article>
  <article class="quote-card abs" style="left:373px">
    <div class="avatar abs" role="img" aria-label="Portrait photo of the client giving the testimonial"></div>
    <p class="quote-text abs">Lorem ipsum dolor sit amet, consectetur adipiscing elit. Nam facilisis mollis laoreet. Ut luctus dui vitae scelerisque scelerisque. Donec ullamcorper viverra urna. Suspendisse pulvinar gravida nibh, vitae pharetra nunc faucibus vestibulum. Suspendisse</p>
    <p class="quote-name abs">Jhone Doe</p>
    <p class="quote-role abs">Contatnry Popilar sit</p>
  </article>
</section>

<footer class="site-footer abs">
  <h4 class="footer-heading abs" style="left:61px">WHO WE ARE</h4>
  <p class="footer-text abs" style="left:61px;top:45px;width:135px">Lorem ipsum dolor sit amet, consectetur adipiscing elit. Nullam venenatis velit blandit est condimentum aliquet. Curabitur ut libero justo. Nulla ut ex facilisis, tincidunt quam vitae, iaculis orci. Nullam eu faucibus nibh.</p>
  <div class="more abs">More <svg width="9" height="9" viewBox="0 0 9 9" fill="none" stroke="#fff"><circle cx="4.5" cy="4.5" r="4"/><path d="M3 4.5h3M4.8 3.2l1.3 1.3-1.3 1.3"/></svg></div>

  <h4 class="footer-heading abs" style="left:250px">USEFUL LINKS</h4>
  <ul class="footer-links abs"><li>HOME</li><li>SERVICES</li><li>ABOUT</li><li>OUR WORK</li><li>CONTACT</li></ul>

  <h4 class="footer-heading abs" style="left:372px">GET IN TOUCH</h4>
  <p class="footer-text abs" style="left:373px;top:45px;width:135px">Doloreiur quia commolu ptatemp dolupta oreprerum tibusam eumenis et consent accullignis dentibea</p>
  <div class="contact-line abs" style="top:83px"><svg width="6" height="8" viewBox="0 0 6 8"><path d="M3 0a3 3 0 0 1 3 3c0 2-3 5-3 5S0 5 0 3a3 3 0 0 1 3-3Z" fill="#fff"/></svg><span style="margin-left:4px">48 Harbour Lane, Suite 3<br>Port Alder, Florida 30112</span></div>
  <div class="contact-line abs" style="top:110px"><svg width="7" height="7" viewBox="0 0 9 12"><path d="M2 0h2l1 3-1.5 1c.6 1.6 1.4 2.7 2.5 3.5L7.5 6 9 8.5 8 11c-4 0-7.5-5-8-9.5Z" fill="#fff"/></svg>Phone: 555 204 1187</div>
  <div class="contact-line abs" style="top:122px"><svg width="7" height="5" viewBox="0 0 7 5"><rect width="7" height="5" fill="#fff"/><path d="M0 0l3.5 3L7 0" stroke="#6b7a86" fill="none" stroke-width=".8"/></svg>Email:name@domain.com</div>

  <h4 class="footer-heading abs" style="left:548px">CONTACT</h4>
  <p class="footer-text abs" style="left:549px;top:45px;width:120px">Doloreiur quia commolu ptatemp dolupta oreprerum</p>
  <div class="field abs" style="top:73px">Email</div>
  <div class="field abs" style="top:95px;justify-content:space-between;padding-right:6px">Contact For <svg width="7" height="5" viewBox="0 0 7 5"><path d="M1 1l2.5 2.5L6 1" stroke="#fff" fill="none"/></svg></div>
  <div class="send-btn abs">CONTACT</div>
</footer>

<div class="bottom-bar abs">
  <p class="copyright abs">© 2015 yoursite. All rights reserved.</p>
  <div class="social abs"><span></span><span></span><span></span><span></span></div>
</div>

</body>
</html>
```